Design cd cover for the vocal group: Ember, cd title Harbor Light. Cd cover is for EP release to be followed by full album. Songs are: Silela Nkwe Dumo(Carry the lantern); Under Cedar; Sikhanda(Over the quiet river); When Dawn Came. There is no track entitled harbor light; the concept of the sound of gospel music as embodied in the music tracks - contemporary and traditional - is the basis of the album title.
NB: Project can close Tuesday 12 November to account for the 5 days as I do not count Saturday as a working day.
Hey guys,
Hello to everyone. I would like to take this opportunity to say thank you for your participation. Your submissions have been great and much appreciated. Forgive me for not being able to provide feedback to all of you. The time has come for me to make selection decisions and I would like to say thank you to all for your participation, you have been great and amazing.

```html
<!DOCTYPE html>
<html lang="en">
<head>
<meta charset="utf-8">
<title>Ember – Harbor Light EP Cover</title>
<link rel="stylesheet" href="https://fonts.googleapis.com/css2?family=Lato:wght@400&display=swap">
<style>
  :root {
    --page-bg: #ffffff;
    --sky-top: #8d6f95;
    --sky-mid: #e07a6e;
    --sky-glow: #f4a24c;
    --horizon: #f7cf5a;
    --sea-top: #b77a86;
    --sea-mid: #a26f86;
    --sea-low: #b98596;
    --text-white: #ffffff;
  }
  html, body {
    margin: 0;
    width: 1200px;
    height: 900px;
    overflow: hidden;
    background: var(--page-bg);
  }
  .cover {
    position: absolute;
    left: 235px;
    top: 86px;
    width: 730px;
    height: 730px;
    overflow: hidden;
  }
  .cover-photo {
    position: absolute;
    inset: 0;
    background: linear-gradient(
      to bottom,
      var(--sky-top) 0%,
      var(--sky-mid) 28%,
      var(--sky-glow) 42%,
      var(--horizon) 49%,
      var(--sea-top) 51%,
      var(--sea-mid) 70%,
      var(--sea-low) 100%
    );
  }
  .group-name {
    position: absolute;
    left: 40px;
    top: 56px;
    margin: 0;
    font-family: "Lato", sans-serif;
    font-weight: 400;
    font-size: 92px;
    line-height: 1;
    letter-spacing: 2px;
    color: var(--text-white);
  }
  .ep-title {
    position: absolute;
    left: 44px;
    top: 172px;
    margin: 0;
    font-family: "Lato", sans-serif;
    font-weight: 400;
    font-size: 30px;
    line-height: 1;
    letter-spacing: 4px;
    color: var(--text-white);
  }
  .lead-track {
    position: absolute;
    left: 40px;
    top: 670px;
    margin: 0;
    font-family: "Lato", sans-serif;
    font-weight: 400;
    font-size: 17px;
    line-height: 1.2;
    color: var(--text-white);
  }
</style>
</head>
<body>
  <main class="cover">
    <div class="cover-photo" role="img" aria-label="Long-exposure seascape at sunset: pink and orange sky over a calm misty sea, a dark rocky outcrop at left"></div>
    <h1 class="group-name">Ember</h1>
    <h2 class="ep-title">Harbor Light</h2>
    <p class="lead-track">Silela Nkwe Dumo</p>
  </main>
</body>
</html>
```